Brightpath Holdings Business Card

Create a two sided, high gloss, quality business card for Brightpath Holdings.

Target Market(s)

People wanting to purchase, scale, and sell businesses.

Industry/Entity Type

Entrepreneurs

Contact Information for Business Card

One line: Dana Corwell, CPA, CMA Another line: Entrepreneur & Investor Another line: Business Ownership Transition Expert Another line: Multi-State Licensed Real Estate Broker Phone 954-BRTPATH (278-7284) Email Dana@Brightpath Holdings.com Website www.Brightpath.com

Requirements
Must have
• Black Card, logo on one side, all other information on the other side including a small logo.
Nice to have
• Possibly add a tagline "Helping entrepreneurs live a life they don't need a vacation from"
Should not have
• There will not be a mailing address on these cards.

```html
<!DOCTYPE html>
<html lang="en">
<head>
<meta charset="utf-8">
<title>Brightpath Holdings Business Card</title>
<link href="https://fonts.googleapis.com/css2?family=Montserrat:wght@700;800&family=Open+Sans:wght@400;600&display=swap" rel="stylesheet">
<style>
  :root {
    --backdrop: #3b3b3c;
    --card-black: #0d0d0d;
    --card-edge: #c99a2e;
    --gold-light: #f6e08a;
    --gold-mid: #d9ab3c;
    --gold-dark: #9c7020;
    --text-light: #ececec;
    --pattern-tone: #1a1a1a;
  }
  * { box-sizing: border-box; margin: 0; padding: 0; }
  html, body { width: 1200px; height: 801px; overflow: hidden; }
  body {
    background: var(--backdrop);
    font-family: "Open Sans", Arial, sans-serif;
    position: relative;
  }
  .card {
    position: absolute;
    top: 246px;
    width: 540px;
    height: 309px;
    background: var(--card-black);
    border: 2px solid var(--card-edge);
    overflow: hidden;
  }
  .card-front { left: 40px; }
  .card-back { left: 620px; }

  .brand {
    position: absolute;
    left: 24px;
    top: 34px;
    display: flex;
    align-items: center;
    gap: 8px;
  }
  .brand-dot {
    width: 22px; height: 22px;
    border-radius: 50%;
    background: var(--gold-mid);
  }
  .brand-name {
    font-family: "Montserrat", Arial, sans-serif;
    font-weight: 800;
    font-size: 22px;
    color: var(--gold-mid);
    letter-spacing: 0.3px;
  }

  .portrait {
    position: absolute;
    right: 0;
    top: 0;
    width: 250px;
    height: 220px;
    background: radial-gradient(ellipse at 45% 35%, #7a5a3e 0%, #3a3330 40%, #141418 80%);
  }

  .name-band {
    position: absolute;
    left: 0;
    top: 92px;
    width: 300px;
    height: 32px;
    background: linear-gradient(90deg, var(--gold-dark), var(--gold-light) 45%, var(--gold-mid) 100%);
    display: flex;
    align-items: center;
    padding-left: 24px;
  }
  .person-name {
    font-family: "Montserrat", Arial, sans-serif;
    font-weight: 800;
    font-size: 16px;
    color: #111;
    letter-spacing: 0.3px;
  }
  .person-name .credentials { font-weight: 700; }

  .roles {
    position: absolute;
    left: 24px;
    top: 136px;
    list-style: none;
    color: var(--text-light);
    font-size: 13px;
    line-height: 18px;
  }
  .contacts {
    position: absolute;
    left: 24px;
    top: 206px;
    list-style: none;
    color: var(--text-light);
    font-size: 13px;
    line-height: 20px;
  }
  .contacts li { display: flex; align-items: center; gap: 8px; }
  .contacts svg { width: 11px; height: 11px; fill: var(--gold-mid); flex: none; }

  .back-pattern {
    position: absolute;
    inset: 0;
    background: radial-gradient(circle at 60% 40%, var(--pattern-tone), var(--card-black) 80%);
  }
  .back-mark {
    position: absolute;
    right: 46px;
    top: 128px;
    display: flex;
    align-items: center;
    gap: 6px;
  }
  .back-mark .brand-dot { width: 14px; height: 14px; }
  .back-mark .brand-name { font-size: 14px; }
</style>
</head>
<body>
  <section class="card card-front" aria-label="Business card front">
    <div class="portrait" role="img" aria-label="Portrait photo of Dana Corwell in a dark blazer and yellow shirt"></div>
    <div class="brand">
      <span class="brand-dot"></span>
      <span class="brand-name">Brightpath Holdings</span>
    </div>
    <div class="name-band">
      <span class="person-name">DANA CORWELL, <span class="credentials">CPA, CMA</span></span>
    </div>
    <ul class="roles">
      <li>Entrepreneur &amp; Investor</li>
      <li>Business Ownership Transition Expert</li>
      <li>Multi-State Licensed Real Estate Broker</li>
    </ul>
    <ul class="contacts">
      <li>
        <svg viewBox="0 0 24 24" aria-hidden="true"><path d="M6.6 10.8a15 15 0 0 0 6.6 6.6l2.2-2.2a1 1 0 0 1 1-.25 11.4 11.4 0 0 0 3.6.57 1 1 0 0 1 1 1V20a1 1 0 0 1-1 1A17 17 0 0 1 3 4a1 1 0 0 1 1-1h3.5a1 1 0 0 1 1 1c0 1.25.2 2.45.57 3.57a1 1 0 0 1-.25 1z"/></svg>
        954-BRTPATH (278-7284)
      </li>
      <li>
        <svg viewBox="0 0 24 24" aria-hidden="true"><path d="M2 5h20v14H2z M2 5l10 8 10-8" stroke="#0d0d0d" stroke-width="1.5"/></svg>
        Dana@BrightpathHoldings.com
      </li>
      <li>
        <svg viewBox="0 0 24 24" aria-hidden="true"><circle cx="12" cy="12" r="10"/></svg>
        www.Brightpath.com
      </li>
    </ul>
  </section>

  <section class="card card-back" aria-label="Business card back">
    <div class="back-pattern" role="img" aria-label="Tonal black pattern of repeated compass motifs"></div>
    <div class="back-mark">
      <span class="brand-dot"></span>
      <span class="brand-name">Brightpath</span>
    </div>
  </section>
</body>
</html>
```